Harborline Stay Collective Business Card Design

Design a business card for Harborline Stay Collective. Look at the website for colors and reference. Card should have logo, name, title, office number, mobile number, email, URL and a tagline like, "Luxury Hotel & Resort Email Marketing" (This might change).

https://www.harborlinestaycollective.net

The rest I will leave up to your imagination.

Contact Information for Business Card

Logo, name, title, office number, mobile number, email, URL and a tagline like, "Luxury Hotel & Resort Email Marketing" (This might change).

```html
<!DOCTYPE html>
<html lang="en">
<head>
<meta charset="utf-8">
<title>Harborline Stay Collective — Business Card</title>
<link href="https://fonts.googleapis.com/css2?family=Roboto:wght@400;500&display=swap" rel="stylesheet">
<style>
  :root {
    --backdrop: #e4e4e4;
    --card: #ffffff;
    --ink: #141414;
    --accent: #f07a10;
    --sky: #5b86c9;
    --dusk: #d69a5c;
    --lawn: #4f7a34;
    --sea: #1fa8a8;
    --forest: #4d6b35;
  }
  * { margin: 0; padding: 0; box-sizing: border-box; }
  html, body { width: 1200px; height: 1200px; overflow: hidden; }
  body {
    background: var(--backdrop);
    font-family: "Roboto", Arial, sans-serif;
    color: var(--ink);
    position: relative;
  }
  .card {
    position: absolute;
    left: 190px;
    width: 778px;
    height: 432px;
    background: var(--card);
    border-radius: 20px;
    overflow: hidden;
  }
  .card--front { top: 85px; }
  .card--back { top: 600px; }
  .card__photo {
    position: absolute;
    inset: 0;
    width: 100%;
    height: 100%;
  }
  .brand {
    position: absolute;
    left: 0;
    width: 414px;
    top: 246px;
    height: 34px;
    display: flex;
    align-items: center;
    justify-content: center;
    gap: 10px;
  }
  .brand__mark {
    width: 16px;
    height: 16px;
    background: var(--accent);
    flex: none;
  }
  .brand__name {
    font-size: 26px;
    font-weight: 500;
    color: var(--ink);
    white-space: nowrap;
  }
  .tagline {
    position: absolute;
    left: 0;
    width: 414px;
    top: 323px;
    text-align: center;
    font-size: 24px;
    line-height: 33px;
    font-weight: 400;
  }
  .tagline span { display: block; white-space: nowrap; }
  .person {
    position: absolute;
    right: 49px;
    top: 167px;
    text-align: right;
  }
  .person__name { font-size: 27px; line-height: 32px; font-weight: 400; }
  .person__role { font-size: 22px; line-height: 30px; margin-top: 1px; }
  .contacts {
    position: absolute;
    right: 49px;
    top: 268px;
    list-style: none;
  }
  .contacts li {
    display: flex;
    align-items: center;
    justify-content: flex-end;
    gap: 11px;
    height: 33px;
    font-size: 19.5px;
  }
  .contacts svg { width: 21px; height: 21px; flex: none; }
  .contacts .web { color: var(--accent); }
</style>
</head>
<body>

<section class="card card--front">
  <svg class="card__photo" viewBox="0 0 1150 638" preserveAspectRatio="none">
    <defs>
      <linearGradient id="resortTones" x1="0" y1="0" x2="0" y2="1">
        <stop offset="0" stop-color="var(--sky)"/>
        <stop offset="0.45" stop-color="var(--dusk)"/>
        <stop offset="0.8" stop-color="var(--lawn)"/>
        <stop offset="1" stop-color="#6c7a62"/>
      </linearGradient>
    </defs>
    <path role="img" aria-label="Photo of a luxury resort hotel with palm trees at dusk"
      fill="url(#resortTones)"
      d="M540,0 L1150,0 L1150,535 C1040,565 960,540 880,470 C780,370 700,150 540,0 Z"/>
  </svg>
  <div class="brand">
    <span class="brand__mark"></span>
    <span class="brand__name">Harborline Stay Collective</span>
  </div>
  <p class="tagline">
    <span>Luxury Hotel</span>
    <span>&amp; Resort Email Marketing</span>
  </p>
</section>

<section class="card card--back">
  <svg class="card__photo" viewBox="0 0 1150 638" preserveAspectRatio="none">
    <defs>
      <linearGradient id="coastTones" x1="0" y1="0" x2="0" y2="1">
        <stop offset="0" stop-color="#7fb0dc"/>
        <stop offset="0.3" stop-color="var(--forest)"/>
        <stop offset="0.6" stop-color="var(--sea)"/>
        <stop offset="1" stop-color="#3b6a3a"/>
      </linearGradient>
    </defs>
    <path role="img" aria-label="Photo of a rocky forested coastline above a turquoise cove"
      fill="url(#coastTones)"
      d="M0,0 L970,0 C840,110 770,290 640,400 C490,530 300,600 0,550 Z"/>
  </svg>
  <div class="person">
    <p class="person__name">Daniel MORROW</p>
    <p class="person__role">Fonction</p>
  </div>
  <ul class="contacts">
    <li>+01 234 567 890
      <svg viewBox="0 0 24 24" fill="none" stroke="currentColor" stroke-width="1.5"><path d="M2 9c0-3 20-3 20 0v2h-5V9H7v2H2z"/><path d="M6 11l-2 9h16l-2-9"/><rect x="9" y="13" width="6" height="5"/></svg>
    </li>
    <li>+01 234 567 890
      <svg viewBox="0 0 24 24" fill="none" stroke="currentColor" stroke-width="1.5"><rect x="6" y="1.5" width="12" height="21" rx="2"/><circle cx="12" cy="19" r="0.8" fill="currentColor"/></svg>
    </li>
    <li>info@harborlinestaycollective.net
      <svg viewBox="0 0 24 24" fill="none" stroke="currentColor" stroke-width="1.5"><rect x="2" y="5" width="20" height="14"/><path d="M2 5l10 8 10-8M2 19l7-7M22 19l-7-7"/></svg>
    </li>
    <li class="web">www.harborlinestaycollective.net
      <svg viewBox="0 0 24 24" fill="none" stroke="currentColor" stroke-width="1.5"><circle cx="12" cy="12" r="10"/><ellipse cx="12" cy="12" rx="4.5" ry="10"/><path d="M2 12h20M4 6.5h16M4 17.5h16"/></svg>
    </li>
  </ul>
</section>

</body>
</html>
```